Wine Label for a wine from Tuscany, Italy

We need a wine label for a white and red wine, can be the same label or can be somewhat differentiated with any variation you feel would be good.. These two wines come from Tuscany, Italy. Wine labels from Tuscany Italy tend to be traditional. We are open to traditional looking labels but also more modern, eye catching too. We want to convey a sense of elegance, importance, great wine. I am attaching some examples of labels we like from Tuscany, also a label that was designed for us recently by one of you, which we LOVE. No wine glasses, wine bottles or grapes featured on the label please. We tend to like the white background. No blue please.

Target Market(s)

More women than men purchase wine, but it needs to appeal to both sexes.

Requirements
Must have
• Wine Name: Corte L' or Corte l'
• Type/Varletal: Rosso Toscano (White is Vermentino)
• Vintage (year): 2018
• That is all the text we want on the label, thanks
Nice to have
• Clean, something that makes someone want to grab this wine bottle off the shelf!
Should not have
• Images of Wine glass, wine bottles, grapes
• Do not use the color blue please.

```html
<!DOCTYPE html>
<html lang="en">
<head>
<meta charset="utf-8">
<title>Corte L' – Wine Labels</title>
<link rel="stylesheet" href="https://fonts.googleapis.com/css2?family=Bodoni+Moda:opsz,wght@6..96,400;6..96,500&display=swap">
<style>
  :root {
    --backdrop: #000000;
    --label-paper: #ffffff;
    --estate-gold: #a98542;
    --vermentino-yellow: #ecc91f;
    --rosso-red: #b93526;
    --etching-light: #efe3c8;
    --etching-mid: #d6bd8c;
    --type-white: #ffffff;
  }
  * { margin: 0; padding: 0; box-sizing: border-box; }
  html, body {
    width: 1200px;
    height: 2540px;
    overflow: hidden;
    background: var(--backdrop);
  }
  .label-pair {
    position: absolute;
    top: 841px;
    left: 74px;
    display: flex;
    gap: 96px;
  }
  .wine-label {
    width: 477px;
    height: 858px;
    background: var(--label-paper);
    overflow: hidden;
  }
  .wine-label svg { display: block; width: 477px; height: 858px; }
  .estate-name {
    font-family: "Bodoni Moda", "Times New Roman", serif;
    font-weight: 400;
    font-size: 128px;
    fill: var(--estate-gold);
  }
  .monogram {
    font-family: "Bodoni Moda", "Times New Roman", serif;
    font-weight: 500;
  }
  .wine-label--white .monogram { fill: var(--vermentino-yellow); }
  .wine-label--rosso .monogram { fill: var(--rosso-red); }
  .varietal-line {
    font-family: "Bodoni Moda", "Times New Roman", serif;
    font-weight: 400;
    font-size: 22px;
    letter-spacing: 0.5px;
    fill: var(--type-white);
  }
</style>
</head>
<body>
  <main class="label-pair">
    <article class="wine-label wine-label--white">
      <svg viewBox="0 0 477 858" xmlns="http://www.w3.org/2000/svg">
        <defs>
          <linearGradient id="landscape-white" x1="0" y1="0" x2="0" y2="1">
            <stop offset="0" stop-color="var(--etching-light)"/>
            <stop offset="0.55" stop-color="var(--etching-mid)"/>
            <stop offset="1" stop-color="var(--etching-light)"/>
          </linearGradient>
        </defs>
        <text class="estate-name" x="238" y="242" text-anchor="middle">Corte</text>
        <rect class="landscape" x="0" y="360" width="477" height="420" fill="url(#landscape-white)" role="img" aria-label="Engraved Tuscan landscape with rolling hills, a farmhouse and cypress trees"/>
        <text class="monogram" x="-14" y="812" font-size="740">L</text>
        <text class="monogram" x="405" y="600" font-size="420">’</text>
        <text class="varietal-line" transform="translate(104 792) rotate(-90)">WHITE VERMENTINO . 2018</text>
      </svg>
    </article>
    <article class="wine-label wine-label--rosso">
      <svg viewBox="0 0 477 858" xmlns="http://www.w3.org/2000/svg">
        <defs>
          <linearGradient id="landscape-rosso" x1="0" y1="0" x2="0" y2="1">
            <stop offset="0" stop-color="var(--etching-light)"/>
            <stop offset="0.55" stop-color="var(--etching-mid)"/>
            <stop offset="1" stop-color="var(--etching-light)"/>
          </linearGradient>
        </defs>
        <text class="estate-name" x="238" y="242" text-anchor="middle">Corte</text>
        <rect class="landscape" x="0" y="360" width="477" height="420" fill="url(#landscape-rosso)" role="img" aria-label="Engraved Tuscan landscape with rolling hills, a farmhouse and cypress trees"/>
        <text class="monogram" x="-14" y="812" font-size="740">L</text>
        <text class="monogram" x="405" y="600" font-size="420">’</text>
        <text class="varietal-line" transform="translate(104 792) rotate(-90)">ROSSO TOSCANO  /  2018</text>
      </svg>
    </article>
  </main>
</body>
</html>
```